Vantor 7 Rower Vinyl Designs and Vantor Vinyl ArcVane Designs

We would like to have a great design for our Rowers and ArcVanes. The background of the stickers should be dark. Fade or structure is possible. Use our CI Booklet for Fonts, Colors and Logo.

```html
<!DOCTYPE html>
<html lang="en">
<head>
<meta charset="utf-8">
<title>Vantor 7 Rower and ArcVane Vinyl Designs</title>
<link rel="stylesheet" href="https://fonts.googleapis.com/css2?family=Archivo:wght@500;600;800;900&display=swap">
<style>
  :root {
    --page: #ffffff;
    --ink: #0a0a0a;
    --panel-black: #0a0b0d;
    --panel-navy: #101a2a;
    --navy-glow: #15436b;
    --dome-black: #0e1216;
    --dome-navy: #112233;
    --white: #f4f6f8;
    --grey: #7f7f7f;
    --brand-blue: #154170;
  }
  * { box-sizing: border-box; margin: 0; padding: 0; }
  html, body {
    width: 1200px; height: 1200px; overflow: hidden;
    background: var(--page);
    font-family: "Archivo", Arial, sans-serif;
  }
  .sheet { position: relative; width: 1200px; height: 1200px; }

  .machine-label {
    position: absolute; top: 140px; width: 430px;
    text-align: center; font-weight: 800; font-size: 44px;
    letter-spacing: 0.5px; color: var(--ink); line-height: 1;
  }

  .sticker {
    position: absolute; top: 210px; width: 430px; height: 788px;
    overflow: hidden;
  }
  .sticker--rower { left: 134px; background: var(--panel-black); }
  .sticker--arcvane {
    left: 644px;
    background:
      radial-gradient(ellipse 330px 260px at 100% 0%, var(--navy-glow) 0%, rgba(21,67,107,0.45) 45%, rgba(16,26,42,0) 100%),
      var(--panel-navy);
  }

  .dome { position: absolute; left: 0; top: 490px; width: 430px; height: 298px; }
  .sticker--rower .dome path { fill: var(--dome-black); }
  .sticker--arcvane .dome path { fill: var(--dome-navy); }

  .brand {
    position: absolute; left: 46px; top: 70px;
    display: flex; align-items: center; gap: 14px;
  }
  .brand-dot { width: 46px; height: 46px; border-radius: 50%; background: var(--brand-blue); flex: none; }
  .brand-name {
    color: var(--white); font-weight: 600; font-size: 22px;
    line-height: 1.1; letter-spacing: 1.5px;
  }

  .headline { position: absolute; left: 44px; top: 0; white-space: nowrap; }
  .headline span {
    position: absolute; left: 0; display: block; line-height: 1;
    text-shadow: 0 6px 18px rgba(0,0,0,0.55);
  }
  .line-1 { top: 458px; font-size: 92px; font-weight: 500; color: var(--white); }
  .line-2 { top: 541px; font-size: 92px; font-weight: 500; color: var(--grey); }
  .line-3 { top: 630px; font-size: 74px; font-weight: 900; color: var(--brand-blue); letter-spacing: 1px; }

  .accent-bar {
    position: absolute; left: 46px; top: 503px;
    width: 90px; height: 6px; background: var(--brand-blue);
  }
</style>
</head>
<body>
<main class="sheet">
  <h2 class="machine-label" style="left:134px">ROWER</h2>
  <h2 class="machine-label" style="left:644px">ARCVANE</h2>

  <section class="sticker sticker--rower" aria-label="Rower vinyl design">
    <svg class="dome" viewBox="0 0 430 298" aria-hidden="true">
      <path d="M0 44 C120 -10 310 -10 430 44 L430 298 L0 298 Z"/>
    </svg>
    <div class="brand">
      <span class="brand-dot"></span>
      <span class="brand-name">HALDEN<br>PERFORMANCE</span>
    </div>
    <h1 class="headline">
      <span class="line-1">EARN</span>
      <span class="line-2">YOUR</span>
      <span class="line-3">METERS</span>
    </h1>
    <div class="accent-bar" style="top:713px"></div>
  </section>

  <section class="sticker sticker--arcvane" aria-label="ArcVane vinyl design">
    <svg class="dome" viewBox="0 0 430 298" aria-hidden="true">
      <path d="M0 44 C120 -10 310 -10 430 44 L430 298 L0 298 Z"/>
    </svg>
    <div class="brand">
      <span class="brand-dot"></span>
      <span class="brand-name">HALDEN<br>PERFORMANCE</span>
    </div>
    <h1 class="headline">
      <span class="line-1">PULL</span>
      <span class="line-2">WITH</span>
      <span class="line-3">POWER</span>
    </h1>
    <div class="accent-bar" style="top:713px"></div>
  </section>
</main>
</body>
</html>
```